Mortgage Broker Site

Need a custom design for a mortgage broker site - please refer to the attached Word .doc that gives more detail.

Number of Pages Required

5+ page

Colors

Designer to choose colors to be used in the design.

```html
<!DOCTYPE html>
<html lang="en">
<head>
<meta charset="utf-8">
<title>Brightway Mortgage</title>
<link href="https://fonts.googleapis.com/css2?family=Montserrat:wght@400;600;700;800&family=Open+Sans:wght@400;600&display=swap" rel="stylesheet">
<style>
:root{
  --red:#c8202f;
  --red-dark:#a51824;
  --navy:#1d2733;
  --ink:#2b2f36;
  --muted:#7a8089;
  --line:#e3e6ea;
  --blue:#2f8fd8;
  --blue-dark:#2479bd;
  --paper:#ffffff;
  --soft:#f4f6f8;
}
*{box-sizing:border-box;margin:0;padding:0}
html,body{width:786px;height:1200px;overflow:hidden;background:var(--paper)}
body{font-family:"Open Sans",Arial,sans-serif;color:var(--ink);position:relative}
.btn{display:inline-block;background:var(--red);color:#fff;font:700 7px/1 "Montserrat",Arial,sans-serif;letter-spacing:.6px;text-transform:uppercase;padding:8px 13px;border-radius:2px;white-space:nowrap}

/* header */
.site-header{position:absolute;top:0;left:0;width:786px;height:45px;background:#fff;display:flex;align-items:center;padding:0 38px 0 40px;border-bottom:1px solid var(--line);z-index:2}
.brand{display:flex;align-items:center;gap:6px;font:800 17px/1 "Montserrat",Arial,sans-serif;color:var(--red);white-space:nowrap}
.brand-mark{width:11px;height:11px;background:var(--red)}
.main-nav{margin-left:auto;display:flex;gap:20px;align-items:center;font:600 6.5px/1 "Montserrat",Arial,sans-serif;text-transform:uppercase;color:var(--navy);letter-spacing:.4px}
.main-nav .btn{padding:7px 12px}

/* hero */
.hero{position:absolute;top:45px;left:0;width:786px;height:322px}
.hero-photo{position:absolute;inset:0;background:linear-gradient(100deg,#6f8fb3 0%,#9fb7cf 38%,#d8c3b0 62%,#c79c83 80%,#8fa6bd 100%)}
.hero-shade{position:absolute;inset:0;background:linear-gradient(90deg,rgba(20,40,70,.55) 0%,rgba(20,40,70,.25) 45%,rgba(0,0,0,0) 70%)}
.hero-copy{position:absolute;left:132px;top:88px;width:320px;color:#fff}
.hero-copy h1{font:800 26px/1.1 "Montserrat",Arial,sans-serif;text-transform:uppercase;letter-spacing:.3px;white-space:nowrap}
.hero-copy p{font-size:7px;line-height:1.55;margin:12px 0 16px;width:290px;opacity:.95}
.hero-actions{display:flex;gap:8px}
.btn-ghost{background:transparent;border:1px solid #fff}

/* tools */
.tools{position:absolute;top:367px;left:0;width:786px;height:328px;background:#fff;text-align:center}
.section-title{display:inline-block;margin-top:44px;font:800 13px/1 "Montserrat",Arial,sans-serif;text-transform:uppercase;color:var(--navy);padding:6px 12px;border-bottom:3px solid var(--red);border-left:1px solid var(--red);border-right:1px solid var(--red)}
.tools-intro{font-size:7px;line-height:1.6;color:var(--muted);width:260px;margin:12px auto 0}
.tool-cards{display:flex;justify-content:center;gap:20px;margin-top:22px}
.tool-card{width:164px;height:140px;background:#fff;box-shadow:0 2px 10px rgba(0,0,0,.12);padding:26px 16px 0}
.tool-card svg{display:block;margin:0 auto}
.tool-card h3{font:700 10px/1 "Montserrat",Arial,sans-serif;color:var(--navy);margin:12px 0 7px}
.tool-card p{font-size:6px;line-height:1.55;color:var(--muted)}

/* limits */
.limits{position:absolute;top:695px;left:0;width:786px;height:210px}
.limits-photo{position:absolute;inset:0;background:linear-gradient(120deg,#8b8f95 0%,#c9c6c0 40%,#a7a49f 70%,#6e7278 100%)}
.limits-shade{position:absolute;inset:0;background:rgba(25,28,34,.68)}
.limits-body{position:relative;text-align:center;color:#fff;padding-top:54px}
.limits-body h2{font:700 14px/1.2 "Montserrat",Arial,sans-serif;text-transform:uppercase}
.limits-body p{font-size:7.5px;line-height:1.55;width:420px;margin:8px auto 0;opacity:.9}
.search{display:flex;justify-content:center;margin-top:22px}
.search-field{width:180px;height:18px;background:#fff;border-radius:2px 0 0 2px}
.search .btn{height:18px;padding:6px 14px;border-radius:0 2px 2px 0}

/* connect */
.connect{position:absolute;top:905px;left:0;width:786px;height:105px;text-align:center;overflow:hidden;background:#fff}
.skyline{position:absolute;left:0;right:0;bottom:0;height:60px;background:linear-gradient(180deg,rgba(215,220,228,0) 0%,#dfe4ea 100%)}
.connect h2{position:relative;margin-top:32px;font:700 13px/1 "Montserrat",Arial,sans-serif;color:var(--navy)}
.connect .btn{position:relative;margin-top:12px;padding:6px 12px}

/* footer */
.site-footer{position:absolute;top:1010px;left:0;width:786px;height:190px;background:var(--blue);color:#fff}
.footer-brand{position:absolute;left:130px;top:34px}
.footer-brand .brand{color:#fff;font-size:19px}
.footer-brand .brand-mark{background:#fff;width:12px;height:12px}
.socials{display:flex;gap:6px;margin-top:12px;padding-left:8px}
.socials span{width:10px;height:10px;border-radius:50%;background:#fff;opacity:.9}
.footer-col{position:absolute;top:28px;font-size:6px;line-height:1.75;white-space:nowrap}
.footer-col h4{font:700 6.5px/1 "Montserrat",Arial,sans-serif;text-transform:uppercase;margin-bottom:6px;letter-spacing:.4px}
.col-links{left:300px}.col-company{left:480px}.col-policies{left:610px}
.footer-bottom{position:absolute;left:130px;top:140px;font-size:5.5px;line-height:1.6;width:420px;opacity:.9}
.to-top{position:absolute;left:630px;top:146px;width:18px;height:18px;background:#fff;display:flex;align-items:center;justify-content:center}
</style>
</head>
<body>

<header class="site-header">
  <div class="brand"><span class="brand-mark"></span>Brightway</div>
  <nav class="main-nav">
    <span>Home</span><span>Rates</span><span>Purchase</span><span>Refinance</span><span>Schedule a Call</span><span>Owners</span>
    <span class="btn">Apply Now</span>
  </nav>
</header>

<section class="hero">
  <div class="hero-photo" role="img" aria-label="Photo of a smiling family of three outdoors under a blue sky"></div>
  <div class="hero-shade"></div>
  <div class="hero-copy">
    <h1>Mortgage Rates Are<br>At All Time Lows!</h1>
    <p>Lock in today's low rates with a local broker who compares dozens of lenders for you, so you can buy or refinance with confidence and keep more money in your pocket every month.</p>
    <div class="hero-actions"><span class="btn">Purchase Rates</span><span class="btn btn-ghost">Refinance Rates</span></div>
  </div>
</section>

<section class="tools">
  <h2 class="section-title">Mortgage Tools</h2>
  <p class="tools-intro">Use our simple tools below to estimate your monthly payment and see what your home may be worth today.</p>
  <div class="tool-cards">
    <div class="tool-card">
      <svg width="32" height="32" viewBox="0 0 32 32" aria-hidden="true">
        <rect x="6" y="3" width="20" height="26" rx="2" fill="none" stroke="#1d2733" stroke-width="1.6"/>
        <rect x="9" y="6" width="14" height="6" fill="#c8202f"/>
        <g fill="#1d2733"><rect x="9" y="15" width="3" height="3"/><rect x="14.5" y="15" width="3" height="3"/><rect x="20" y="15" width="3" height="3"/><rect x="9" y="20" width="3" height="3"/><rect x="14.5" y="20" width="3" height="3"/><rect x="20" y="20" width="3" height="6" fill="#c8202f"/><rect x="9" y="25" width="3" height="1.5"/><rect x="14.5" y="25" width="3" height="1.5"/></g>
      </svg>
      <h3>Mortgage Calculator</h3>
      <p>See how much house you can afford and what your monthly payment is likely to be.</p>
    </div>
    <div class="tool-card">
      <svg width="32" height="32" viewBox="0 0 32 32" aria-hidden="true">
        <path d="M4 16 L16 5 L28 16" fill="none" stroke="#c8202f" stroke-width="2"/>
        <rect x="8" y="15" width="16" height="13" fill="none" stroke="#1d2733" stroke-width="1.6"/>
        <rect x="14" y="20" width="4" height="8" fill="#c8202f"/>
      </svg>
      <h3>Home Value Checker</h3>
      <p>Get a quick estimate of your home's value using recent local sales and trends.</p>
    </div>
  </div>
</section>

<section class="limits">
  <div class="limits-photo" role="img" aria-label="Photo of loan paperwork, a calculator and a pen on a desk"></div>
  <div class="limits-shade"></div>
  <div class="limits-body">
    <h2>2019 Mortgage Loan Limits for Conventional, FHA, &amp; VA Loans</h2>
    <p>Mortgage loan limits for every U.S. county as published by national lending agencies, covering conventional, FHA and VA home loans.</p>
    <div class="search"><span class="search-field"></span><span class="btn">Search</span></div>
  </div>
</section>

<section class="connect">
  <div class="skyline" role="img" aria-label="Faint city skyline illustration"></div>
  <h2>Connect With America's Lending Experts Today!</h2>
  <span class="btn">Find The Rate</span>
</section>

<footer class="site-footer">
  <div class="footer-brand">
    <div class="brand"><span class="brand-mark"></span>Brightway</div>
    <div class="socials"><span></span><span></span><span></span></div>
  </div>
  <div class="footer-col col-links">
    <h4>Links</h4>
    <div>Today's Mortgage Rates</div><div>Loan Types</div><div>Loan Calculator</div><div>Home Value Checker</div>
  </div>
  <div class="footer-col col-company">
    <h4>Company</h4>
    <div>About Us</div><div>Careers</div><div>Contact Us</div>
  </div>
  <div class="footer-col col-policies">
    <h4>Policies</h4>
    <div>Privacy Policy</div><div>Terms of Use</div><div>Licensing</div><div>Disclosures</div>
  </div>
  <div class="footer-bottom">Brightway Mortgage. Equal Housing Opportunity. All rights reserved.<br>Copyright 2019. Rates and programs are subject to change without notice.</div>
  <div class="to-top"><svg width="8" height="8" viewBox="0 0 8 8" aria-hidden="true"><path d="M1 6 L4 2 L7 6" fill="none" stroke="#2f8fd8" stroke-width="1.5"/></svg></div>
</footer>

</body>
</html>
```